Need to drive pregnant women to my 3d4d ultrasound studio where i provide 4d ultrasound with hyperalistic imaging and gender reveals

Industry/Entity Type

Healthcare

Font styles to use
Decorative
Script

Requirements
Must have
• My Company name Latido de Luna 4D. EVERYTHING HAS TO BE IN SPANISH
Nice to have
• SIMPLE AND NOT TOO BUSY
Should not have
• website

```html
<!DOCTYPE html>
<html lang="es">
<head>
<meta charset="utf-8">
<title>Latido de Luna 4D – Banner</title>
<link rel="stylesheet" href="https://fonts.googleapis.com/css2?family=Dancing+Script:wght@700&family=Roboto:wght@500;900&display=swap">
<style>
  :root {
    --backdrop: #a0a0a0;
    --banner-black: #000000;
    --banner-shine: #4a4b4d;
    --headline: #ffffff;
    --tagline-bg: #e9e9ea;
    --tagline-text: #111111;
    --frame-line: #f2e6dc;
    --scan-dark: #5a2a08;
    --scan-mid: #b8661e;
    --scan-light: #e09a4a;
    --skin-dark: #4a2c30;
    --skin-mid: #d79b8c;
    --skin-light: #f3cfc2;
  }
  * { margin: 0; padding: 0; box-sizing: border-box; }
  html, body {
    width: 1200px;
    height: 600px;
    overflow: hidden;
    background: var(--backdrop);
  }
  .banner {
    position: absolute;
    left: 79px;
    top: 154px;
    width: 1043px;
    height: 304px;
    background:
      linear-gradient(150deg, transparent 0%, transparent 30%, rgba(74,75,77,0.9) 48%, transparent 70%),
      radial-gradient(ellipse 320px 180px at 330px 120px, var(--banner-shine), transparent 75%),
      var(--banner-black);
    font-family: "Roboto", Arial, sans-serif;
    overflow: hidden;
  }
  .headline {
    position: absolute;
    left: 43px;
    top: 28px;
    color: var(--headline);
    line-height: 1;
    font-weight: normal;
  }
  .headline-top {
    display: block;
    font-family: "Dancing Script", "Brush Script MT", cursive;
    font-weight: 700;
    font-size: 74px;
    line-height: 0.9;
  }
  .headline-bottom {
    display: block;
    margin-top: 8px;
    font-family: "Roboto", Arial, sans-serif;
    font-weight: 900;
    font-size: 133px;
    letter-spacing: 1px;
    line-height: 0.82;
    text-transform: uppercase;
  }
  .tagline {
    position: absolute;
    left: 34px;
    top: 231px;
    width: 594px;
    height: 33px;
    background: var(--tagline-bg);
    color: var(--tagline-text);
    font-weight: 500;
    font-size: 19px;
    line-height: 33px;
    padding-left: 12px;
    white-space: nowrap;
    overflow: hidden;
  }
  .gallery {
    position: absolute;
    left: 659px;
    top: 34px;
    width: 351px;
    height: 230px;
    border: 1px solid var(--frame-line);
    display: flex;
  }
  .gallery-photo {
    flex: 1;
    height: 100%;
  }
  .gallery-photo--scan {
    background: radial-gradient(ellipse at 45% 55%, var(--scan-light), var(--scan-mid) 45%, var(--scan-dark) 100%);
    border-right: 1px solid var(--frame-line);
  }
  .gallery-photo--newborn {
    background: radial-gradient(ellipse at 45% 50%, var(--skin-light), var(--skin-mid) 60%, var(--skin-dark) 100%);
  }
</style>
</head>
<body>
  <section class="banner">
    <h1 class="headline">
      <span class="headline-top">Latido de</span>
      <span class="headline-bottom">Luna 4D</span>
    </h1>
    <p class="tagline">Ecografía 4D con imágenes hiperrealistas y revelación de sexo</p>
    <div class="gallery">
      <div class="gallery-photo gallery-photo--scan" role="img" aria-label="Ecografía 4D en tonos ámbar de un bebé en el vientre"></div>
      <div class="gallery-photo gallery-photo--newborn" role="img" aria-label="Fotografía de un recién nacido dormido"></div>
    </div>
  </section>
</body>
</html>
```